Otter Vale pipe restorations recruiting business card

We need a recruiting business card for our commercial pipe line company “Otter Vale” that reaches out to individuals looking for a job or who would be a great fit to our team. We want to include:
- Recognizing the candidates potential
—> You are amazing!
- Capture who we are (name, subtitle, tag line & our core values)
—> OTTER VALE, Pipe Restoration Solutions, INVESTIGATE | PLAN | DELIVER | , our values: Family, Integrity, Generosity, Faith, Humility, Communication, Collaboration, Innovation, Mission Minded, Positivity, Improvement, Fulfillment, Fun and Diversity
3. Call to action (apply at website/email this address/call this number to become apart of our team/family)
—> If you are interested in a career with a fully funded startup that is using technology and a new and innovative approach to the age old art of plumbing we are seeking team members who appreciate hard work and want to be part of a winning team!
—> send your resume to: recruiting@ottervale.example
4. Personal point of reference (let them know x [person handing out card writes their name] sent you! )
—> Let them know that _______________ sent you!
Call me if you have any questions _________________

Contact Information for Business Card

Front: Explaining who we are/core values
Back: recruitment explanation

Font styles to use
Serif
Sans Serif

```html
<!DOCTYPE html>
<html lang="en">
<head>
<meta charset="utf-8">
<title>Otter Vale – Recruiting Card</title>
<link href="https://fonts.googleapis.com/css2?family=Montserrat:wght@300;400;500;700&display=swap" rel="stylesheet">
<style>
  :root {
    --stage: #5b5b5b;
    --card-dark: #2f2e2f;
    --card-light: #ffffff;
    --ink-light: #ffffff;
    --ink-soft: #e6e6e6;
    --ink-dark: #1e1e1e;
    --accent: #1f6b55;
    --rule: #9a9a9a;
  }
  * { box-sizing: border-box; margin: 0; padding: 0; }
  html, body { width: 1200px; height: 1200px; overflow: hidden; }
  body {
    background: var(--stage);
    font-family: "Montserrat", Arial, sans-serif;
    display: flex; flex-direction: column; align-items: center; justify-content: center;
    gap: 60px;
  }
  .card { width: 700px; height: 400px; position: relative; overflow: hidden; }

  /* Referral side */
  .card--referral { background: var(--card-light); color: var(--ink-dark); }
  .referral-mark {
    position: absolute; left: 50%; top: 92px; width: 58px; height: 58px;
    margin-left: -29px; border-radius: 50%; background: var(--ink-dark);
  }
  .referral-lines { position: absolute; left: 0; right: 0; top: 190px; display: flex; flex-direction: column; align-items: center; gap: 30px; font-size: 17px; }
  .referral-line { display: flex; align-items: flex-end; gap: 12px; }
  .blank { display: inline-block; width: 200px; border-bottom: 1.5px solid var(--ink-dark); height: 18px; }

  /* Recruiting side */
  .card--recruit { background: var(--card-dark); color: var(--ink-light); }
  .brand { position: absolute; top: 34px; left: 0; right: 0; display: flex; justify-content: center; align-items: center; gap: 16px; }
  .brand-mark { width: 64px; height: 64px; border-radius: 50%; background: var(--ink-light); }
  .brand-name { font-size: 40px; font-weight: 500; letter-spacing: 1px; line-height: 1; }
  .brand-sub { font-size: 11.5px; font-weight: 300; letter-spacing: 1.2px; line-height: 1.35; margin-top: 4px; }
  .values { position: absolute; top: 122px; left: 40px; right: 40px; text-align: center; }
  .values-title { font-size: 12px; font-weight: 400; letter-spacing: 1px; }
  .values-list { font-size: 12px; font-weight: 400; line-height: 1.45; margin-top: 4px; color: var(--ink-soft); }
  .values-rule { width: 44px; height: 2px; background: var(--ink-light); margin: 10px auto 0; }
  .pitch { position: absolute; top: 208px; left: 46px; right: 46px; text-align: center; font-size: 15px; line-height: 1.45; }

  .contact { position: absolute; left: 0; right: 0; bottom: 0; height: 74px; display: flex; align-items: center; }
  .tab { width: 74px; height: 66px; background: var(--accent); display: flex; align-items: center; justify-content: center; }
  .tab--mail { border-top-right-radius: 34px; align-self: flex-end; }
  .tab--web { border-top-left-radius: 34px; border-bottom-left-radius: 34px; width: 64px; height: 54px; align-self: flex-start; margin-top: -6px; }
  .contact-item { padding-left: 16px; }
  .contact-item--web { margin-left: auto; text-align: right; padding: 0 16px 0 0; }
  .contact-label { font-size: 10.5px; font-weight: 300; letter-spacing: 1px; }
  .contact-value { font-size: 20px; font-weight: 700; }
  .contact-divider { width: 1px; height: 44px; background: var(--rule); margin-left: 34px; }
</style>
</head>
<body>

  <section class="card card--referral">
    <div class="referral-mark"></div>
    <div class="referral-lines">
      <p class="referral-line">Let them know that <span class="blank"></span> sent you!</p>
      <p class="referral-line">Call me <span class="blank"></span> if you have any questions?</p>
    </div>
  </section>

  <section class="card card--recruit">
    <header class="brand">
      <div class="brand-mark"></div>
      <div>
        <div class="brand-name">OTTER VALE</div>
        <div class="brand-sub">PIPE RESTORATION SOLUTIONS<br>INVESTIGATE • PLAN • DELIVER</div>
      </div>
    </header>

    <div class="values">
      <p class="values-title">OUR VALUES</p>
      <p class="values-list">Family, Integrity, Generosity, Faith, Humility, Communication, Collaboration,<br>Innovation, Mission Minded, Positivity, Improvement, Fulfillment, Fun and Diversity</p>
      <div class="values-rule"></div>
    </div>

    <p class="pitch">If you are interested in a career with a fully funded startup that is using technology and a new and innovative approach to the age old art of plumbing we are seeking team members who appreciate hard work and want to be part of a winning team!</p>

    <footer class="contact">
      <div class="tab tab--mail">
        <svg width="34" height="24" viewBox="0 0 34 24" fill="none" stroke="#fff" stroke-width="1.6"><rect x="1" y="1" width="32" height="22"/><path d="M1 1 L17 14 L33 1 M1 23 L13 11 M33 23 L21 11"/></svg>
      </div>
      <div class="contact-item">
        <p class="contact-label">SEND YOUR RESUME TO</p>
        <p class="contact-value">recruiting@ottervale.example</p>
      </div>
      <div class="contact-divider"></div>
      <div class="contact-item contact-item--web">
        <p class="contact-label">OUR WEBSITE</p>
        <p class="contact-value">www.ottervale.example</p>
      </div>
      <div class="tab tab--web">
        <svg width="26" height="26" viewBox="0 0 26 26" fill="none" stroke="#fff" stroke-width="1.5"><circle cx="13" cy="13" r="11"/><ellipse cx="13" cy="13" rx="5" ry="11"/><path d="M2 13 H24 M4 7 H22 M4 19 H22"/></svg>
      </div>
    </footer>
  </section>

</body>
</html>
```